Business cards for a new business: Amber Willow Dawn Healing

I would like for the card to include a lotus. The business is a healing practice so I'd like the overall colours to be pink and green and for it to have a soft feel. The name of the practice is
"Amber Willow Dawn Healing", which I'd like to be included, as well as the words: "Energetic and spiritual healing to restore health, harmony and wellbeing". Also, my name - Tovan and the number: 5319 6048

Target Market(s)

Everyone interested in personal healing!

Industry/Entity Type

Business

Contact Information for Business Card

As above……..could be single or double-sided
I'd like the font for the name of the practice and my name to be in green and be a flowing, but simple font - elegant.
The background to be a light pink. See below for colours

Colors
f9d9e8
eea4c8
e567a6
d0ebe7
86cfc6
33b7a4

Requirements
Must have
• See above
Nice to have
• See above

```html
<!DOCTYPE html>
<html lang="en">
<head>
<meta charset="utf-8">
<title>Amber Willow Dawn Healing – Business Card</title>
<link rel="stylesheet" href="https://fonts.googleapis.com/css2?family=Yanone+Kaffeesatz:wght@300&family=Cabin:wght@400&display=swap">
<style>
  :root {
    --stage: #f2eef0;
    --pink-light: #f9d9e8;
    --pink-mid: #eea4c8;
    --pink-deep: #e567a6;
    --green-light: #d0ebe7;
    --green-mid: #86cfc6;
    --green-deep: #33b7a4;
    --white: #ffffff;
  }
  html, body {
    margin: 0;
    padding: 0;
    width: 1200px;
    height: 900px;
    overflow: hidden;
    background: var(--stage);
  }
  .card {
    position: absolute;
    left: 357px;
    top: 47px;
    width: 488px;
    height: 805px;
    overflow: hidden;
    background:
      radial-gradient(circle at 55% 12%, rgba(249,217,232,0.9) 0%, rgba(249,217,232,0) 45%),
      radial-gradient(circle at 15% 48%, rgba(238,164,200,0.35) 0%, rgba(238,164,200,0) 12%),
      radial-gradient(circle at 60% 60%, rgba(255,255,255,0.95) 0%, rgba(255,255,255,0) 55%),
      radial-gradient(circle at 40% 95%, rgba(238,164,200,0.45) 0%, rgba(238,164,200,0) 30%),
      linear-gradient(180deg, var(--pink-light) 0%, #fbe7f0 45%, #fdf1f6 70%, var(--pink-light) 100%);
  }
  .practice-name {
    position: absolute;
    margin: 0;
    font-family: "Yanone Kaffeesatz", sans-serif;
    font-weight: 300;
    font-size: 60px;
    line-height: 1;
    color: var(--green-deep);
    letter-spacing: 0.5px;
  }
  .practice-name .line-one {
    position: absolute;
    left: 78px;
    top: 56px;
    white-space: nowrap;
  }
  .practice-name .line-two {
    position: absolute;
    left: 184px;
    top: 128px;
    white-space: nowrap;
  }
  .divider {
    position: absolute;
    left: 229px;
    width: 30px;
    height: 8px;
    border-radius: 4px;
    background: var(--green-deep);
    opacity: 0.8;
  }
  .divider.top { top: 226px; }
  .divider.bottom { top: 360px; }
  .tagline {
    position: absolute;
    left: 0;
    top: 247px;
    width: 488px;
    margin: 0;
    text-align: center;
    font-family: "Cabin", sans-serif;
    font-size: 25px;
    line-height: 34px;
    color: var(--green-deep);
  }
  .lotus-art {
    position: absolute;
    left: 52px;
    top: 406px;
    width: 384px;
    height: 316px;
    display: block;
  }
  .contact {
    position: absolute;
    left: 0;
    top: 741px;
    width: 488px;
    margin: 0;
    text-align: center;
    font-family: "Cabin", sans-serif;
    font-size: 25px;
    color: var(--green-deep);
  }
</style>
</head>
<body>
  <main class="card">
    <h1 class="practice-name">
      <span class="line-one">Amber Willow</span>
      <span class="line-two">Dawn Healing</span>
    </h1>

    <div class="divider top" role="img" aria-label="Small ornament mark"></div>
    <p class="tagline">Energetic and spiritual healing<br>to restore<br>health, harmony and wellbeing</p>
    <div class="divider bottom" role="img" aria-label="Small ornament mark"></div>

    <svg class="lotus-art" viewBox="0 0 384 316" role="img" aria-label="Illustration of a pink lotus flower with green leaves">
      <defs>
        <radialGradient id="lotusGlow" cx="50%" cy="45%" r="55%">
          <stop offset="0%" stop-color="#e567a6"/>
          <stop offset="45%" stop-color="#eea4c8"/>
          <stop offset="100%" stop-color="#f9d9e8" stop-opacity="0"/>
        </radialGradient>
        <radialGradient id="leafGlow" cx="50%" cy="50%" r="50%">
          <stop offset="0%" stop-color="#86cfc6"/>
          <stop offset="100%" stop-color="#d0ebe7" stop-opacity="0"/>
        </radialGradient>
      </defs>
      <ellipse cx="192" cy="150" rx="192" ry="150" fill="url(#lotusGlow)"/>
      <ellipse cx="192" cy="282" rx="160" ry="34" fill="url(#leafGlow)"/>
    </svg>

    <p class="contact">Tovan: (02) 5319 6048</p>
  </main>
</body>
</html>
```